The Corvanta Group's website for high impact furniture promotions

I am looking for a simple website. we are a promotional company that runs events for furniture stores to increase sales for short periods of time. i would like the website to have about 4 areas to explain our company. I would like it to be simple and user friendly. I would like a link to chatterbook and a contact section. I am attaching our logo that i would like somewhere large or possibly in the backround. I am open to different color schemes. I would like to convey fast paced, modern, reliable. I am open to all different styles and look forward to seeing whats out there. we are looking for a quick turn around, so if we see one that we like quick, we will pick that one thanks
Updates
Project Deadline Extended
Reason: looking for some really creative designs and want to give a fair amount of time to produce
Target Market(s)
Retail Furniture store owners
Industry/Entity Type
It Company
Number of Pages Required
1 page
Colors
Designer to choose colors to be used in the design.
Look and feel
Each slider illustrates characteristics of the customer's brand and the style your logo design should communicate.

```html
<!DOCTYPE html>
<html lang="en">
<head>
<meta charset="utf-8">
<title>The Corvanta Group</title>
<link rel="stylesheet" href="https://fonts.googleapis.com/css2?family=Cinzel:wght@400;500&family=Crimson+Text:wght@400;600;700&family=Roboto:ital,wght@0,400;0,500;1,400&display=swap">
<style>
:root{
  --navy:#1b2130;
  --brown:#8a5a2e;
  --gold:#c99a5c;
  --ink:#2b2b2b;
  --muted:#555;
  --soft:#f4f4f4;
  --line:#e4e4e4;
  --white:#fff;
}
*{box-sizing:border-box;margin:0;padding:0}
html,body{width:1200px;height:2659px;overflow:hidden}
body{position:relative;background:var(--white);font-family:"Roboto",Arial,sans-serif;color:var(--ink)}
.abs{position:absolute}

/* hero */
.hero{left:0;top:0;width:1200px;height:612px;background:linear-gradient(100deg,#3a3836 0%,#55504a 22%,#8a5a34 45%,#6b4326 62%,#4a3a2e 80%,#2d2a28 100%)}
.hero-top{left:0;top:0;width:1200px;height:120px}
.brand{left:140px;top:10px;width:160px;text-align:center;color:var(--gold);font-family:"Cinzel",serif}
.brand-mark{display:block;width:56px;height:56px;border-radius:50%;background:var(--gold);margin:0 auto 8px}
.brand-name{font-size:13px;letter-spacing:1.5px;line-height:1.3;text-transform:uppercase}
.nav{right:152px;top:20px;display:flex;align-items:center;gap:14px;font-family:"Crimson Text",serif;font-size:11.5px;font-weight:600;letter-spacing:.6px;text-transform:uppercase}
.nav a{color:var(--white);text-decoration:none}
.nav a.active{color:var(--gold)}
.nav .dot{width:3px;height:3px;border-radius:50%;background:var(--white)}
.social{width:22px;height:22px;border:1.5px solid var(--white);border-radius:50%;display:inline-block}

/* headings */
.section-title{left:0;width:1200px;text-align:center;font-family:"Cinzel",serif;font-size:32px;color:var(--brown);letter-spacing:1px}
.section-title::after{content:"";display:block;width:46px;height:2px;background:#cfcfcf;margin:10px auto 0}
.section-title.light{color:var(--gold)}
.section-title.light::after{background:rgba(255,255,255,.4)}

/* buttons */
.btn{display:inline-flex;align-items:center;height:28px;border:1.5px solid var(--navy);border-radius:3px;background:var(--white);font-family:"Crimson Text",serif;font-weight:700;font-size:10px;letter-spacing:.6px;text-transform:uppercase;color:var(--navy);text-decoration:none;overflow:hidden}
.btn .btn-icon{width:26px;height:100%;background:var(--navy);display:flex;align-items:center;justify-content:center}
.btn .btn-icon::after{content:"";border-left:7px solid var(--gold);border-top:5px solid transparent;border-bottom:5px solid transparent}
.btn .btn-label{padding:0 12px 0 10px}

/* about */
.about-text{left:160px;top:766px;width:880px;text-align:center;font-size:11.6px;line-height:18px;color:#333}
.about-btn{left:542px;top:890px;height:30px}

/* services */
.card{top:1214px;width:210px;text-align:center}
.card-photo{width:210px;height:134px}
.card-title{font-family:"Crimson Text",serif;font-weight:700;font-size:16px;margin-top:10px;color:var(--ink)}
.card-text{font-size:11px;line-height:15px;color:#333;margin:2px 4px 0}
.card .btn{margin-top:10px;height:26px}

/* testimonials */
.testimonials-bg{left:0;top:1528px;width:1200px;height:572px;background:var(--soft)}
.quote-mark{left:0;top:1790px;width:1200px;text-align:center;font-family:"Crimson Text",serif;font-size:64px;font-weight:700;line-height:1;color:var(--navy)}
.quote-box{left:213px;top:1810px;width:778px;height:152px;background:var(--white);border-radius:6px;padding:36px 36px 0;text-align:center;font-style:italic;font-size:12.2px;line-height:20px;color:#333}
.quote-box::after{content:"";position:absolute;left:377px;bottom:-12px;border-top:12px solid var(--white);border-left:12px solid transparent;border-right:12px solid transparent}
.quote-author{left:0;top:1991px;width:1200px;text-align:center;font-family:"Crimson Text",serif;font-weight:700;font-size:12px}
.slider-arrow{top:1862px;width:24px;height:48px}

/* contact */
.contact{left:0;top:2100px;width:1200px;height:506px;background:linear-gradient(110deg,#3b2e26 0%,#54433a 35%,#4a3a31 65%,#3a2d25 100%)}
.field{background:var(--white);height:32px;padding:0 12px;font-style:italic;font-size:10px;line-height:32px;color:#555}
.field.message{height:119px;line-height:1;padding-top:12px}
.submit{left:144px;top:2474px;width:132px;height:34px;border-radius:3px;background:linear-gradient(#c99a5c,#a87838);color:var(--white);font-family:"Crimson Text",serif;font-weight:700;font-size:12px;letter-spacing:.5px;text-transform:uppercase;display:flex;align-items:center;justify-content:center;gap:8px}
.info{left:767px;top:2256px;width:300px;color:var(--white)}
.info-item{margin-bottom:16px}
.info-label{display:flex;align-items:center;gap:7px;font-family:"Crimson Text",serif;font-weight:700;font-size:12px;text-transform:uppercase;letter-spacing:.5px}
.info-value{font-size:11.5px;line-height:16px;margin-left:18px}
.info .social{width:32px;height:32px;margin-top:2px}

/* footer */
.footer{left:0;top:2606px;width:1200px;height:53px;background:var(--navy);display:flex;align-items:center;padding-left:144px;gap:14px;font-family:"Crimson Text",serif;font-size:11px;letter-spacing:.6px;color:#b9b9b9;text-transform:uppercase}
.footer a{color:#b9b9b9;text-decoration:none}
.footer .dot{width:3px;height:3px;border-radius:50%;background:#b9b9b9}
.footer .copy{text-transform:none}
</style>
</head>
<body>

<header>
  <div class="abs hero" role="img" aria-label="Modern living room with a grey sofa, floor lamp, lounge chair and warm wood-panelled wall"></div>
  <svg class="abs hero-top" viewBox="0 0 1200 120" aria-hidden="true">
    <path d="M0 0H1200V40C900 60 400 40 0 85Z" fill="#1b2130"/>
  </svg>
  <div class="abs brand">
    <span class="brand-mark"></span>
    <div class="brand-name">The Corvanta Group</div>
  </div>
  <nav class="abs nav">
    <a class="active" href="#home">Home</a><span class="dot"></span>
    <a href="#about">About</a><span class="dot"></span>
    <a href="#services">Services</a><span class="dot"></span>
    <a href="#testimonials">Testimonials</a><span class="dot"></span>
    <a href="#contact">Contact</a>
    <a class="social" href="#chatterbook" aria-label="chatterbook"></a>
  </nav>
</header>

<section id="about">
  <h2 class="abs section-title" style="top:696px">Who We Are</h2>
  <p class="abs about-text">Lorem ipsum dolor sit amet, consectetur adipiscing elit. Suspendisse vitae luctus neque, eu cursus ligula. Etiam turpis orci, scelerisque at risus id, sagittis cursus quam. Maecenas rutrum eget massa at tempor. Sed eu risus cursus ante egestas feugiat. Etiam viverra lobortis imperdiet. Nulla faucibus diam ut purus tincidunt pulvinar. Etiam laoreet sem et semper aliquet. Vivamus sed lorem lectus. Donec aliquam felis vitae faucibus pharetra. Vestibulum ultrices efficitur justo egestas ultrices. Nunc et diam erat. Quisque eu porttitor nisi, eu aliquam magna. Nam at arcu massa. Aliquam ultrices sit amet magna nec efficitur. Sed bibendum maximus tincidunt. Integer sit amet volutpat urna, volutpat molestie nibh. Pellentesque vulputate, nisi sed condimentum imperdiet, nisi ex posuere est, vulputate pretium ante felis eget urna. Aliquam at felis quis tortor aliquet volutpat sed ac massa. Fusce commodo facilisis est a sodales. Nulla dapibus venenatis sem ut condimentum. Donec faucibus justo a purus viverra, a cursus nisi scelerisque urabitur ac velit dui raesent maecenas vehicula.</p>
  <a class="abs btn about-btn" href="#about"><span class="btn-icon"></span><span class="btn-label">Learn More</span></a>
</section>

<svg class="abs" style="left:0;top:990px" width="1200" height="150" viewBox="0 0 1200 150" aria-hidden="true">
  <polygon points="0,0 1200,0 1200,134 600,42 0,134" fill="#f4f4f4"/>
  <polyline points="0,142 600,52 1200,142" fill="none" stroke="#e6e6e6" stroke-width="7"/>
  <circle cx="600" cy="42" r="30" fill="#e9e9e9"/>
</svg>

<section id="services">
  <h2 class="abs section-title" style="top:1144px">What We Do</h2>
  <article class="abs card" style="left:144px">
    <div class="card-photo" role="img" aria-label="Hand pointing at colour swatches on a planning table" style="background:linear-gradient(135deg,#6a4a3a,#c7a27a 45%,#d65a6a 70%,#4a6a9a)"></div>
    <h3 class="card-title">Event Planning</h3>
    <p class="card-text">Lorem ipsum dolor sit amet, consectetur adipiscing elit. Suspendisse vitae luctus neque, eu cursus ligula. Etiam turpis orci, scelerisque at risus id, sagittis cursus quam maecenas rutrum eget massa.</p>
    <a class="btn" href="#services"><span class="btn-icon"></span><span class="btn-label">Learn More</span></a>
  </article>
  <article class="abs card" style="left:378px">
    <div class="card-photo" role="img" aria-label="Team of smiling business professionals in an office" style="background:linear-gradient(135deg,#e8e6e4,#c9bfb8 40%,#8a9ab8 70%,#c84a4a)"></div>
    <h3 class="card-title">Event Management</h3>
    <p class="card-text">Sed eu risus cursus ante egestas feugiat. Etiam viverra lobortis imperdiet. Nulla faucibus diam ut purus tincidunt pulvinar. Etiam laoreet sem et semper aliquet vamus sed lorem lectus aliquam felis.</p>
    <a class="btn" href="#services"><span class="btn-icon"></span><span class="btn-label">Learn More</span></a>
  </article>
  <article class="abs card" style="left:612px">
    <div class="card-photo" role="img" aria-label="Consultants reviewing documents together at a desk" style="background:linear-gradient(135deg,#3a4a5a,#8a7a6a 45%,#c8c2ba 70%,#6a5040)"></div>
    <h3 class="card-title">Consultation</h3>
    <p class="card-text">Nunc et diam erat. Quisque eu porttitor nisi, eu aliquam magna liquam ultrices sit amet magna nec efficitur. Sed bibendum maximus tincidunt. Integer sit amet volutpat urna, volutpat molestie nibh.</p>
    <a class="btn" href="#services"><span class="btn-icon"></span><span class="btn-label">Learn More</span></a>
  </article>
  <article class="abs card" style="left:846px">
    <div class="card-photo" role="img" aria-label="Rows of colourful upholstered chairs ready for rental" style="background:linear-gradient(120deg,#d8405a,#e89a3a 35%,#3a8ac8 65%,#7a3a8a)"></div>
    <h3 class="card-title">Equipment Rental</h3>
    <p class="card-text">Pellentesque vulputate, nisi sed condimentum imperdiet, nisi ex posuere est, vulputate pretium ante felis eget urna. Aliquam at felis quis tortor aliquet volutpat sed fusce commodo facilisis est.</p>
    <a class="btn" href="#services"><span class="btn-icon"></span><span class="btn-label">Learn More</span></a>
  </article>
</section>

<section id="testimonials">
  <div class="abs testimonials-bg"></div>
  <svg class="abs" style="left:0;top:1520px" width="1200" height="140" viewBox="0 0 1200 140" aria-hidden="true">
    <polygon points="0,0 1200,0 1200,8 600,95 0,8" fill="#ffffff"/>
    <polyline points="0,18 600,105 1200,18" fill="none" stroke="#e6e6e6" stroke-width="7"/>
    <circle cx="600" cy="105" r="30" fill="#e9e9e9"/>
  </svg>
  <h2 class="abs section-title" style="top:1728px">Kind Words</h2>
  <div class="abs quote-mark">&ldquo;</div>
  <blockquote class="abs quote-box">Lorem ipsum dolor sit amet, consectetur adipiscing elit. Curabitur at nulla quis arcu placerat tincidunt ut non magna. Aenean nec neque vitae tortor rutrum ultricies in ut tortor. Suspendisse sodales vitae felis sed tristique. Pellentesque tincidunt nisl sed elit viverra, eget semper leo euismod. Etiam imperdiet orci eu ex ullamcorper pulvinar. Morbi tristique orci vitae tempus malesuada. Sed efficitur lorem metus, nec accumsan elit venenatis non. Donec scelerisque turpis at aliquam rutrum neque endrerit semper lobortis faucibus.</blockquote>
  <p class="abs quote-author">John Doe / Title / Company</p>
  <svg class="abs slider-arrow" style="left:143px" viewBox="0 0 24 48" aria-label="Previous"><polyline points="20,2 4,24 20,46" fill="none" stroke="#bdbdbd" stroke-width="1.5"/></svg>
  <svg class="abs slider-arrow" style="left:1033px" viewBox="0 0 24 48" aria-label="Next"><polyline points="4,2 20,24 4,46" fill="none" stroke="#bdbdbd" stroke-width="1.5"/></svg>
</section>

<section id="contact">
  <div class="abs contact" role="img" aria-label="Furniture showroom with people browsing, softly darkened"></div>
  <svg class="abs" style="left:0;top:2100px" width="1200" height="506" viewBox="0 0 1200 506" aria-hidden="true">
    <path d="M420 506C700 480 1000 400 1200 230V506Z" fill="#1b2130" opacity=".92"/>
  </svg>
  <h2 class="abs section-title light" style="top:2186px">Get In Touch</h2>
  <div class="abs field" style="left:144px;top:2256px;width:296px">Name*</div>
  <div class="abs field" style="left:448px;top:2256px;width:296px">Company</div>
  <div class="abs field" style="left:144px;top:2299px;width:296px">Email*</div>
  <div class="abs field" style="left:448px;top:2299px;width:296px">Phone</div>
  <div class="abs field message" style="left:144px;top:2340px;width:600px">Message*</div>
  <div class="abs submit">
    <svg width="12" height="12" viewBox="0 0 12 12" aria-hidden="true"><path d="M0 5L12 0L8 12L6 7Z" fill="#fff"/></svg>Submit
  </div>
  <div class="abs info">
    <div class="info-item">
      <div class="info-label"><svg width="11" height="11" viewBox="0 0 12 12" aria-hidden="true"><path d="M2 0L4.5 0L5.5 3L4 4.5C4.8 6.3 5.7 7.2 7.5 8L9 6.5L12 7.5V10C12 11 11 12 10 12C4.5 11.5 0.5 7.5 0 2C0 1 1 0 2 0Z" fill="#fff"/></svg>Phone</div>
      <div class="info-value">555 342 0198</div>
    </div>
    <div class="info-item">
      <div class="info-label"><svg width="11" height="9" viewBox="0 0 12 9" aria-hidden="true"><rect width="12" height="9" fill="#fff"/><polyline points="0,0 6,5 12,0" fill="none" stroke="#3b2e26" stroke-width="1.2"/></svg>Email</div>
      <div class="info-value">info@corvantapromotions.com</div>
    </div>
    <div class="info-item">
      <div class="info-label"><svg width="11" height="13" viewBox="0 0 10 13" aria-hidden="true"><path d="M5 0A5 5 0 0 1 10 5C10 8 5 13 5 13S0 8 0 5A5 5 0 0 1 5 0Z" fill="#fff"/><circle cx="5" cy="5" r="2" fill="#3b2e26"/></svg>Address</div>
      <div class="info-value">6124 Larkspur Ln.<br>Brookfield, North Carolina 27000</div>
    </div>
    <a class="social" href="#chatterbook" aria-label="chatterbook"></a>
  </div>
</section>

<footer class="abs footer">
  <a href="#home">Home</a><span class="dot"></span>
  <a href="#about">About</a><span class="dot"></span>
  <a href="#services">Services</a><span class="dot"></span>
  <a href="#testimonials">Testimonials</a><span class="dot"></span>
  <a href="#contact">Contact</a><span class="dot"></span>
  <span class="copy">&copy;2017 The Corvanta Group.</span>
</footer>

</body>
</html>
```